Holvik Cabinets Quality Custom Built Kitchens, Vanity Units, Robes ect

Hi,
Was after a new design for our business cards,
we are a cabinet making business and pride ourselves in quality custom built Kitchens, Vanity units, robes ect.
we have been around for over 20 years and we are trying to modernize our card logo.
Looking for something eye catching, bold and exciting
family ran and operated business, we work with builders and also have a large private clientel.

Thanks

Industry/Entity Type

Business

Contact Information for Business Card

Holvik Cabinets

Font styles to use
Serif
Script

Requirements
Must have
• Corinne 0461735928 hvcabinets@mailvane.com
• Po Box 2786
• 5B Wattlebark Court Kelbrook Vic 3871
• Phone (03)59286417 Fax (03) 59286942
Nice to have
• Made-to-Measure Kitchens, Vanities & Robes

```html
<!DOCTYPE html>
<html lang="en">
<head>
<meta charset="utf-8">
<title>Holvik Cabinets – Business Card</title>
<link rel="stylesheet" href="https://fonts.googleapis.com/css2?family=Cinzel:wght@700&family=Crimson+Text:ital@1&family=Montserrat:wght@400;600&display=swap">
<style>
  :root {
    --bg: #e7e4df;
    --white: #ffffff;
    --orange: #f39423;
    --brown: #c07028;
    --tan: #c2ae7f;
    --tan-light: #b8946c;
    --shadow: rgba(0,0,0,0.18);
  }
  * { margin: 0; padding: 0; box-sizing: border-box; }
  html, body { width: 1200px; height: 1000px; overflow: hidden; }
  body { background: var(--bg); position: relative; }

  .card {
    position: absolute;
    left: 237px;
    width: 725px;
    height: 425px;
    background: var(--white);
    box-shadow: 0 6px 18px var(--shadow);
    overflow: hidden;
  }
  .card--back { top: 40px; }
  .card--front { top: 525px; }

  .card__shapes { position: absolute; inset: 0; width: 100%; height: 100%; }

  .wordmark {
    position: absolute;
    display: flex;
    align-items: center;
    gap: 14px;
  }
  .wordmark__square {
    width: 30px; height: 30px;
    background: var(--orange);
    flex: none;
  }
  .wordmark__name {
    font-family: "Montserrat", sans-serif;
    font-weight: 600;
    color: var(--brown);
    white-space: nowrap;
  }
  .tagline {
    position: absolute;
    font-family: "Crimson Text", serif;
    font-style: italic;
    color: var(--tan-light);
    white-space: nowrap;
  }

  /* back side */
  .card--back .wordmark { left: 0; right: 0; top: 165px; justify-content: center; }
  .card--back .wordmark__name { font-size: 40px; }
  .card--back .tagline { left: 0; right: 0; top: 228px; text-align: center; font-size: 22px; }

  /* front side */
  .card--front .wordmark { left: 170px; top: 72px; }
  .card--front .wordmark__name { font-size: 34px; }
  .card--front .tagline { left: 214px; top: 120px; font-size: 19px; }

  .contact-name {
    position: absolute;
    left: 150px; width: 485px;
    top: 200px;
    text-align: center;
    font-family: "Cinzel", serif;
    font-weight: 700;
    font-size: 32px;
    color: var(--white);
    letter-spacing: 1px;
  }
  .contact-email, .contact-address, .contact-phones {
    position: absolute;
    font-family: "Montserrat", sans-serif;
    font-size: 14.5px;
    line-height: 21px;
    white-space: nowrap;
  }
  .contact-email { left: 150px; width: 420px; top: 264px; text-align: center; color: var(--brown); font-size: 15px; }
  .contact-address { left: 33px; top: 356px; color: var(--brown); }
  .contact-phones { right: 30px; top: 334px; text-align: right; color: var(--white); }
</style>
</head>
<body>

<section class="card card--back" aria-label="Business card back">
  <div class="wordmark">
    <span class="wordmark__square"></span>
    <span class="wordmark__name">Holvik Cabinets</span>
  </div>
  <p class="tagline">Made-to-Measure Kitchens, Vanities &amp; Robes</p>
</section>

<section class="card card--front" aria-label="Business card front">
  <svg class="card__shapes" viewBox="0 0 725 425" aria-hidden="true">
    <polygon points="0,0 62,0 125,62 0,190" fill="var(--tan)"/>
    <polygon points="725,100 725,425 400,425" fill="var(--brown)"/>
    <rect x="110" y="187" width="545" height="71" fill="var(--brown)"/>
    <polygon points="0,110 45,65 155,178 0,335" fill="var(--orange)"/>
  </svg>

  <div class="wordmark">
    <span class="wordmark__square"></span>
    <span class="wordmark__name">Holvik Cabinets</span>
  </div>
  <p class="tagline">Made-to-Measure Kitchens, Vanities &amp; Robes</p>

  <p class="contact-name">Corinne</p>
  <p class="contact-email">hvcabinets@mailvane.com</p>
  <p class="contact-address">Po Box 2786<br>5B Wattlebark Court Kelbrook Vic 3871</p>
  <p class="contact-phones">Mob: 0461 735 928<br>Phone: (03)59286417<br>Fax: (03) 59286942</p>
</section>

</body>
</html>
```